HVAC company business card design

We need a business card design for a HVAC company. The design must look professional. Both sides will be used. The total data to be on the business card is
Name
Position
Email
Direct Phone/Moile Phone
Company Contacts /Address, Phone, Fax, web)
All data will be submit once the design is confirmed. For generic purposes use;
Emre Toksoy
Managing Director
+902324815263 (Mobile)
4712 Sokak No: 9 KBSE Yenikent IZMIR TURKEY
Tel: +902324815263 Fax : +902324815269
www.luvon.com.tr

Target Market(s)

HVAC

Industry/Entity Type

Business

Contact Information for Business Card

The total data to be on the business card is
Name
Position
Email
Direct Phone/Moile Phone
Emre Toksoy
Managing Director
+902324815263 (Mobile)
www.luvon.com.tr
The BC will use both sides of the card. The front will include the full logo and the details for the business card holder. The business card can be divided into vertical/horizontal or to a special shape. The common data like the company address/phone/fax should be indicated elsewehere. The back can contain some part or the whole logo and must contain the web address.

Font styles to use
Serif
Sans Serif

Colors
0355a3
cfdfed

Requirements
Should not have
• Please be careful with the fonts, it shouldnt be too small or too big and must not interfere with the logo fonts. If you need to use a curvy shape please do not use as the logo is already curvy or use the curves from the logo (if it looks good, otherwise forget it)
• We are not in favor of pictograms, only if they are perfect use them.

```html
<!DOCTYPE html>
<html lang="en">
<head>
<meta charset="utf-8">
<title>LUVON – Business Card</title>
<link rel="stylesheet" href="https://fonts.googleapis.com/css2?family=Montserrat:wght@400;500;600;700&display=swap">
<style>
  :root {
    --bg: #2b2d31;
    --card: #ffffff;
    --navy: #3f4a6a;
    --blue: #2f6bc4;
    --ink: #3a3f4e;
    --muted: #5a6072;
    --tint: #cfdfed;
  }
  * { box-sizing: border-box; margin: 0; padding: 0; }
  html, body { width: 1200px; height: 900px; overflow: hidden; }
  body {
    background: var(--bg);
    font-family: "Montserrat", sans-serif;
    color: var(--ink);
    position: relative;
  }
  .card {
    position: absolute;
    left: 280px;
    width: 640px;
    height: 366px;
    background: var(--card);
    border-radius: 18px;
    overflow: hidden;
    box-shadow: 0 12px 30px rgba(0,0,0,.35);
  }
  .card--back { top: 60px; }
  .card--front { top: 474px; }
  .card__shapes { position: absolute; inset: 0; width: 100%; height: 100%; }

  /* back */
  .brand-mark {
    position: absolute;
    left: 0; right: 0; top: 120px;
    display: flex; align-items: center; justify-content: center; gap: 18px;
  }
  .brand-mark__dot { width: 54px; height: 54px; border-radius: 50%; background: var(--blue); }
  .brand-mark__name { font-size: 56px; font-weight: 700; color: var(--navy); letter-spacing: 2px; }
  .back-web {
    position: absolute; left: 26px; bottom: 12px;
    color: #fff; font-size: 17px; font-weight: 500; letter-spacing: .5px;
  }

  /* front */
  .front-brand {
    position: absolute; left: 56px; top: 78px;
    display: flex; align-items: center; gap: 14px;
  }
  .front-brand__dot { width: 40px; height: 40px; border-radius: 50%; background: var(--blue); }
  .front-brand__name { font-size: 44px; font-weight: 700; color: var(--navy); letter-spacing: 2px; }
  .holder {
    position: absolute; right: 26px; top: 120px; text-align: right;
  }
  .holder__name { font-size: 20px; font-weight: 700; color: var(--blue); }
  .holder__role { font-size: 10.5px; font-weight: 500; color: var(--muted); letter-spacing: 1px; margin-top: 2px; }
  .contacts {
    position: absolute; left: 36px; top: 240px;
    font-size: 11.5px; line-height: 14px; color: var(--muted);
  }
  .contacts li { list-style: none; display: flex; align-items: center; gap: 8px; }
  .contacts .icon { width: 10px; height: 10px; flex: none; fill: var(--blue); }
  .contacts .pad { padding-left: 18px; }
</style>
</head>
<body>

<section class="card card--back" aria-label="Card back">
  <svg class="card__shapes" viewBox="0 0 640 366" preserveAspectRatio="none" aria-hidden="true">
    <polygon points="0,318 238,318 262,338 640,318 640,330 266,366 0,366" fill="var(--navy)"/>
    <polygon points="262,338 640,300 640,318 266,352" fill="var(--blue)"/>
  </svg>
  <div class="brand-mark">
    <span class="brand-mark__dot"></span>
    <span class="brand-mark__name">LUVON</span>
  </div>
  <p class="back-web">www.luvon.com.tr</p>
</section>

<section class="card card--front" aria-label="Card front">
  <svg class="card__shapes" viewBox="0 0 640 366" preserveAspectRatio="none" aria-hidden="true">
    <line x1="30" y1="168" x2="640" y2="168" stroke="var(--navy)" stroke-width="1.5"/>
    <line x1="20" y1="232" x2="560" y2="232" stroke="var(--navy)" stroke-width="1"/>
    <polygon points="566,246 640,246 640,304 548,304" fill="var(--navy)"/>
    <polygon points="130,366 640,366 640,304 548,304 530,344 150,354" fill="var(--blue)"/>
    <polygon points="150,354 530,344 548,304 640,304 640,312 552,312 536,350 150,360" fill="#fff"/>
  </svg>

  <div class="front-brand">
    <span class="front-brand__dot"></span>
    <span class="front-brand__name">LUVON</span>
  </div>

  <div class="holder">
    <p class="holder__name">Emre Toksoy</p>
    <p class="holder__role">MANAGING DIRECTOR</p>
  </div>

  <ul class="contacts">
    <li><svg class="icon" viewBox="0 0 10 10"><rect x="2.5" y="0" width="5" height="10" rx="1"/></svg>+902324815263</li>
    <li><svg class="icon" viewBox="0 0 10 10"><path d="M2 0l2 2-1 2c1 1 2 2 3 3l2-1 2 2-1 2C4 10 0 6 0 1z"/></svg>+902324815263</li>
    <li><svg class="icon" viewBox="0 0 10 10"><rect x="0" y="2" width="10" height="7" rx="1"/><rect x="2" y="0" width="6" height="2"/></svg>+902324815269</li>
    <li><svg class="icon" viewBox="0 0 10 10"><path d="M0 2h10v7H0z M0 2l5 4 5-4" stroke="#fff" stroke-width=".8"/></svg>info@emretoksoy.com.tr</li>
    <li><svg class="icon" viewBox="0 0 10 10"><circle cx="5" cy="5" r="5"/><path d="M0 5h10M5 0c-3 3-3 7 0 10M5 0c3 3 3 7 0 10" stroke="#fff" stroke-width=".7" fill="none"/></svg>www.luvon.com.tr</li>
    <li class="pad">4712 Sokak</li>
    <li class="pad">No: 9 KBSE Yenikent IZMIR TURKEY</li>
  </ul>
</section>

</body>
</html>
```